Marlowvane Services Website Design

We have most content but require a professional design. We have a logo already and will need it utilized along with several of the photos from the attached documentation.
First page should have our mission and Vision and the synapsis provided in the word document. Visitors will be prompted to select from one of our 3 divisions from this page.
Each division will have the same list of tabs : About, Services, Safety, Careers and Contact.
Photos on each divisions page should be representative of the divisions offerings. The word doc attached contains the requested content and we are open to edits that would complement and fill the website.
I like the Tornwick site www.tornwick-example.com - they are our competition so cant be modeled directly after this.
Please include prompts to request quote at each service page. align the format of the geotechnical page to the other 2 divisions.
I used chat gpt for some of the content so will need it optimized for SCO.

```html
<!DOCTYPE html>
<html lang="en">
<head>
<meta charset="utf-8">
<title>Marlowvane Services</title>
<link rel="stylesheet" href="https://fonts.googleapis.com/css2?family=Michroma&family=Roboto:wght@400;500;700&display=swap">
<style>
:root{
  --red:#ed1c24;
  --ink:#222222;
  --text:#444444;
  --muted:#666666;
  --light:#f0f0f0;
  --mist:#ebebeb;
  --footer:#2b2b2b;
  --white:#ffffff;
}
*{margin:0;padding:0;box-sizing:border-box}
html,body{width:1200px;height:3653px;overflow:hidden}
body{position:relative;font-family:"Roboto",Arial,sans-serif;color:var(--text);background:var(--white)}
.abs{position:absolute}
.display{font-family:"Michroma",Arial,sans-serif;color:var(--ink);letter-spacing:1px}
.btn{position:absolute;background:var(--red);color:var(--white);font:700 14px/1 "Roboto",Arial,sans-serif;display:flex;align-items:center;justify-content:center;letter-spacing:.3px}

/* header */
.site-header{position:absolute;left:0;top:0;width:1200px;height:95px;background:var(--white);border-top:4px solid var(--red)}
.brand{position:absolute;left:112px;top:32px;font-family:"Michroma",Arial,sans-serif;font-size:27px;color:var(--red);letter-spacing:1px}
.nav a{position:absolute;top:48px;font-size:15px;color:var(--text);text-decoration:none}
.search{position:absolute;left:1058px;top:42px}

/* hero */
.hero{position:absolute;left:0;top:95px;width:1200px;height:600px;background:linear-gradient(100deg,#3d3631 0%,#6b5e52 45%,#8a7a68 70%,#a09482 100%)}
.hero-truck{position:absolute;left:660px;top:40px;width:320px;height:360px;background:linear-gradient(160deg,#d9dde2,#9aa3ab);opacity:.55;border-radius:8px}
.hero-welcome{position:absolute;left:110px;top:152px;font-family:"Michroma",Arial,sans-serif;font-size:23px;color:var(--white);letter-spacing:1px}
.hero-name{position:absolute;left:108px;top:198px;font-family:"Michroma",Arial,sans-serif;font-size:52px;color:var(--red);letter-spacing:1px}
.hero-text{position:absolute;left:110px;top:292px;width:490px;font-size:15px;line-height:27px;color:var(--white);text-align:justify}
.dots{position:absolute;left:562px;top:546px;display:flex;gap:8px;align-items:center}
.dots i{width:10px;height:10px;border-radius:50%;background:var(--white);display:block}
.dots i.on{width:16px;height:16px;background:var(--red);border:3px solid var(--white)}

/* services */
.services{position:absolute;left:0;top:695px;width:1200px;height:532px;background:var(--light)}
.section-title{position:absolute;width:1200px;text-align:center;font-family:"Michroma",Arial,sans-serif;font-size:30px;color:var(--ink);letter-spacing:1px}
.service-card{position:absolute;top:163px;width:304px}
.service-card .photo{width:304px;height:230px;border-radius:6px}
.service-card h3{margin-top:22px;font-size:25px;font-weight:500;color:var(--ink)}
.arrow{position:absolute;top:253px;width:50px;height:50px;border-radius:50%;display:flex;align-items:center;justify-content:center}

/* vision */
.vision-photo{position:absolute;left:112px;top:1343px;width:430px;height:465px;background:linear-gradient(180deg,#4e6b3e 0%,#7b8f5c 45%,#8c7f6c 70%,#6e655a 100%)}
.red-block{position:absolute;left:356px;top:1577px;width:224px;height:271px;background:var(--red)}
.blueprint{position:absolute;left:978px;top:1475px;width:222px;height:440px;background:linear-gradient(180deg,#f5f6f7,#eceeef);opacity:.8}
.body-text{font-size:17px;line-height:30px;color:var(--text)}

/* mission */
.mission{position:absolute;left:0;top:1960px;width:1200px;height:771px;background:var(--mist)}
.ghost-name{position:absolute;left:20px;top:182px;font-family:"Michroma",Arial,sans-serif;font-size:72px;color:#f2c9cb;letter-spacing:2px;white-space:nowrap;width:520px;overflow:hidden}
.mission-photo{position:absolute;left:550px;top:74px;width:519px;height:521px;background:linear-gradient(180deg,#9a9a8a 0%,#7d8590 40%,#b4b7bb 70%,#8b8f92 100%)}
.mission-card{position:absolute;left:126px;top:346px;width:522px;height:351px;background:var(--white);border-radius:6px;box-shadow:0 4px 14px rgba(0,0,0,.08);padding:48px 30px 0 36px}
.mission-card h2{font-family:"Michroma",Arial,sans-serif;font-size:27px;color:var(--ink);font-weight:400;letter-spacing:1px}
.mission-card p{margin-top:24px;font-size:13.6px;line-height:25.8px;text-align:justify;color:var(--text)}

/* divisions */
.division{position:absolute;top:2943px;width:301px;height:231px;padding:0 16px}
.division.card{background:var(--white);border-top:4px solid var(--red);border-radius:6px;box-shadow:0 3px 14px rgba(0,0,0,.08)}
.division h3{font-size:25px;font-weight:500;color:var(--ink);margin-top:12px}
.division p{font-size:12px;line-height:21px;color:var(--muted);margin-top:12px}
.division .more{display:block;margin-top:10px;font-size:13px;font-weight:700;color:var(--red)}
.division svg{margin-top:18px;display:block}

/* footer */
.site-footer{position:absolute;left:0;top:3287px;width:1200px;height:366px;background:var(--footer);color:var(--white)}
.foot-links{position:absolute;top:128px;width:200px;text-align:center;font-size:15px;line-height:26px}
.foot-rule{position:absolute;top:88px;width:1px;height:234px;background:#555}
.foot-brand{position:absolute;left:0;width:1200px;top:88px;text-align:center;font-family:"Michroma",Arial,sans-serif;font-size:30px;color:var(--red);letter-spacing:1px}
.email{position:absolute;left:438px;top:152px;width:324px;height:44px;background:#3d3d3d;border-radius:3px;font-size:16px;color:#dddddd;padding:13px 18px}
.socials{position:absolute;left:497px;top:236px;display:flex;gap:9px}
.socials span{width:35px;height:35px;border:1.5px solid var(--white);border-radius:50%;display:block}
.copy{position:absolute;left:0;width:1200px;top:305px;text-align:center;font-size:14px}
</style>
</head>
<body>

<header class="site-header">
  <div class="brand">MARLOWVANE</div>
  <nav class="nav">
    <a style="left:589px">About</a>
    <a style="left:671px">Services</a>
    <a style="left:771px">Safety</a>
    <a style="left:857px">Careers</a>
    <a style="left:951px">Contact</a>
  </nav>
  <svg class="search" width="30" height="30" viewBox="0 0 30 30" aria-label="Search"><circle cx="12" cy="12" r="10" fill="none" stroke="#ed1c24" stroke-width="2"/><line x1="19.5" y1="19.5" x2="27" y2="27" stroke="#ed1c24" stroke-width="2.2" stroke-linecap="round"/></svg>
</header>

<section class="hero" role="img" aria-label="Aerial view of a white boom truck parked on a dirt lot">
  <div class="hero-truck"></div>
  <div class="hero-welcome">WELCOME TO</div>
  <div class="hero-name">MARLOWVANE</div>
  <p class="hero-text">At Marlowvane, our mission is to deliver unparalleled aerial access, geotechnical drilling, and service and maintenance solutions, consistently exceeding our clients' expectations.</p>
  <a class="btn" style="left:110px;top:399px;width:125px;height:45px">GET A QUOTE</a>
  <div class="dots"><i></i><i></i><i class="on"></i></div>
</section>

<section class="services">
  <h2 class="section-title" style="top:80px">MARLOWVANE SERVICES</h2>
  <div class="arrow" style="left:45px;background:var(--red)"><svg width="30" height="14" viewBox="0 0 30 14"><path d="M29 7H2M8 1L2 7l6 6" fill="none" stroke="#fff" stroke-width="1.6"/></svg></div>
  <div class="arrow" style="left:1105px;background:var(--white);box-shadow:0 2px 8px rgba(0,0,0,.12)"><svg width="30" height="14" viewBox="0 0 30 14"><path d="M1 7h27M22 1l6 6-6 6" fill="none" stroke="#ed1c24" stroke-width="1.6"/></svg></div>
  <div class="service-card" style="left:112px">
    <div class="photo" role="img" aria-label="Forklift carrying a wrapped crate in a warehouse" style="background:linear-gradient(135deg,#6f6a63,#c9ab86 60,#8a7b6c)"></div>
    <h3>Delivering Safe</h3>
  </div>
  <div class="service-card" style="left:448px">
    <div class="photo" role="img" aria-label="Aerial night view of an oil and gas terminal with storage tanks" style="background:linear-gradient(160deg,#2d4a6a,#5e6f7a 55%,#c49a55)"></div>
    <h3>Oil&amp;Gas</h3>
  </div>
  <div class="service-card" style="left:784px">
    <div class="photo" role="img" aria-label="Construction site with tower cranes under a blue sky" style="background:linear-gradient(180deg,#4f8fc9,#9fc3e0 60%,#a39a8c)"></div>
    <h3>Construction</h3>
  </div>
</section>

<svg class="abs" style="left:56px;top:1289px" width="164" height="150" viewBox="0 0 164 150" aria-hidden="true">
  <g fill="#555">
    <circle cx="4" cy="4" r="2"/><circle cx="22" cy="4" r="2"/><circle cx="40" cy="4" r="2"/><circle cx="58" cy="4" r="2"/><circle cx="76" cy="4" r="2"/><circle cx="94" cy="4" r="2"/><circle cx="112" cy="4" r="2"/><circle cx="130" cy="4" r="2"/><circle cx="148" cy="4" r="2"/>
    <circle cx="4" cy="22" r="2"/><circle cx="22" cy="22" r="2"/><circle cx="40" cy="22" r="2"/><circle cx="58" cy="22" r="2"/><circle cx="76" cy="22" r="2"/><circle cx="94" cy="22" r="2"/><circle cx="112" cy="22" r="2"/><circle cx="130" cy="22" r="2"/><circle cx="148" cy="22" r="2"/>
    <circle cx="4" cy="40" r="2"/><circle cx="22" cy="40" r="2"/><circle cx="40" cy="40" r="2"/><circle cx="58" cy="40" r="2"/><circle cx="76" cy="40" r="2"/><circle cx="94" cy="40" r="2"/><circle cx="112" cy="40" r="2"/><circle cx="130" cy="40" r="2"/><circle cx="148" cy="40" r="2"/>
    <circle cx="4" cy="58" r="2"/><circle cx="22" cy="58" r="2"/><circle cx="40" cy="58" r="2"/>
    <circle cx="4" cy="76" r="2"/><circle cx="22" cy="76" r="2"/><circle cx="40" cy="76" r="2"/>
    <circle cx="4" cy="94" r="2"/><circle cx="22" cy="94" r="2"/><circle cx="40" cy="94" r="2"/>
    <circle cx="4" cy="112" r="2"/><circle cx="22" cy="112" r="2"/><circle cx="40" cy="112" r="2"/>
    <circle cx="4" cy="130" r="2"/><circle cx="22" cy="130" r="2"/><circle cx="40" cy="130" r="2"/>
  </g>
</svg>
<div class="red-block"></div>
<div class="vision-photo" role="img" aria-label="White boom truck on a muddy forest road"></div>
<div class="blueprint" role="img" aria-label="Faint technical drawing of an aerial work basket"></div>
<h2 class="abs display" style="left:686px;top:1424px;font-size:30px;font-weight:400">OUR VISION</h2>
<p class="abs body-text" style="left:686px;top:1500px;width:392px">To be the leading provider of aerial access, geotechnical drilling, and service solutions, setting the standard for excellence in safety, efficiency, and environmental stewardship.</p>
<a class="btn" style="left:686px;top:1662px;width:128px;height:47px">LEARN MORE</a>

<section class="mission">
  <div class="ghost-name" aria-hidden="true">MARLOWVANE</div>
  <div class="mission-photo" role="img" aria-label="Worker in an aerial bucket above a small town holding a for-hire sign"></div>
  <div class="mission-card">
    <h2>MISSION STATEMENT</h2>
    <p>At Marlowvane, our mission is to deliver unparalleled aerial access, geotechnical drilling, and service and maintenance solutions, consistently exceeding our clients' expectations. We strive to achieve this by investing in cutting-edge technology, fostering a culture of safety and continuous improvement, and prioritizing environmental sustainability. Through collaboration, integrity, and dedication, we aim to contribute to the success of our clients while maintaining the highest standards of quality and professionalism.</p>
  </div>
</section>

<h2 class="section-title" style="top:2834px">SELECT DIVISION</h2>

<div class="division card" style="left:118px">
  <svg width="62" height="62" viewBox="0 0 62 62" aria-hidden="true" fill="none" stroke="#555" stroke-width="1.6"><path d="M6 56h34M10 56l4-8h20l4 8M18 48l-4-14h8l6 14M16 34L48 8M44 4h10v8H44z"/></svg>
  <h3>Aerial Access</h3>
  <p>Lorem ipsum dolor elit, sed do eiusmo tempor incididunt ut labore et dolore magna aliqua ut enim ad minim veniam, quis nostrud.</p>
</div>
<div class="division" style="left:452px">
  <svg width="58" height="58" viewBox="0 0 58 58" aria-hidden="true" fill="none" stroke="#ed1c24" stroke-width="1.8"><path d="M18 4h22v8H18zM22 12h14v10H22zM29 22v18M24 40h10l-5 8zM6 54h46M14 48h30v6H14z"/></svg>
  <h3 style="color:var(--red)">Geotechnical Drilling</h3>
  <p>Lorem ipsum dolor elit, sed do eiusmo tempor incididunt ut labore et dolore magna aliqua ut enim ad minim veniam, quis nostrud.</p>
  <a class="more">Learn More &raquo;</a>
</div>
<div class="division card" style="left:786px">
  <svg width="60" height="60" viewBox="0 0 60 60" aria-hidden="true" fill="none" stroke="#555" stroke-width="1.6"><path d="M10 56h24M16 56l6-44M28 56l-6-44M17 44h10M19 30h6M8 12h40M40 12l10 14M44 18l-2 10M42 28h10v6H42z"/></svg>
  <h3>Renewable Energy</h3>
  <p>Lorem ipsum dolor elit, sed do eiusmo tempor incididunt ut labore et dolore magna aliqua ut enim ad minim veniam, quis nostrud.</p>
</div>

<footer class="site-footer">
  <div class="foot-links" style="left:121px">About<br>Services<br>Safety<br>Careers<br>Contact</div>
  <div class="foot-rule" style="left:340px"></div>
  <div class="foot-brand">MARLOWVANE</div>
  <div class="email">Email
    <svg class="abs" style="right:16px;top:14px" width="16" height="16" viewBox="0 0 16 16" aria-hidden="true"><path d="M1 8L15 1 11 15 8 9z" fill="#ed1c24"/></svg>
  </div>
  <div class="socials">
    <span aria-label="Social link"></span><span aria-label="Social link"></span><span aria-label="Social link"></span><span aria-label="Social link"></span><span aria-label="Social link"></span>
  </div>
  <div class="copy">©Copyrights 2024 Marlowvane &nbsp;| &nbsp;&nbsp;All Rights Reserved</div>
  <div class="foot-rule" style="left:859px"></div>
  <div class="foot-links" style="left:873px;top:100px">Terms &amp; Conditions<br>Privacy Policy<br>About Us<br>Support</div>
</footer>

</body>
</html>
```